negocio de venta de lenceria necesita un diseño de empaque para las prendas

somos una empresa mexicana llamada Tavrela, necesitamos un diseño de empaque para productos de lencería casual y sexy, son productos como pantimedias, medias, ligueros, pijamas, bodystockings, nuestros colores actuales son blanco y negro, pero nos gustaría probar diseños mas juveniles o colores un poco mas vivos, adjuntamos unos de nuestros empaques actuales junto con unas fotos de nuestros artículos, tratar de que el diseño se pueda usar en los distintos tipos de prendas que tenemos,

Target Market(s)

muejeres de 18 a 50 años de edad

Industry/Entity Type

ropa interior, lencería, pijamas

Requirements
Must have
• foto de el modelo especifico en la parte frontal del empaque
Nice to have
• me gustaría que el diseño de empaque se pudiera compartir entre los distintos tipo de ropa que tenemos,
Should not have
• no me gustaria que los acabados sean mates o muy obscuros

```html
<!DOCTYPE html>
<html lang="es">
<head>
<meta charset="UTF-8">
<title>Tavrela · Empaque de lencería</title>
<link href="https://fonts.googleapis.com/css2?family=Josefin+Sans:wght@300;400;600&display=swap" rel="stylesheet">
<style>
  :root{
    --stage:#9b9b9b;
    --cream:#f1eee2;
    --cream-deep:#e7e4d4;
    --sage:#c9d8c4;
    --lilac:#e2d3e6;
    --olive:#7a6d48;
    --photo:#b9ad86;
    --ink:#2b2a26;
    --label-edge:#9fd0e6;
    --pink:#e9a9c9;
    --gold:#e6d67a;
  }
  *{box-sizing:border-box;margin:0;padding:0}
  html,body{width:1200px;height:1200px;overflow:hidden}
  body{background:var(--stage);font-family:'Josefin Sans',sans-serif;color:var(--ink);position:relative}

  .package{position:absolute;top:90px;width:500px;height:1020px}
  .package--back{left:60px}
  .package--front{left:640px}

  .hang-tab{
    position:absolute;left:0;top:0;width:100%;height:160px;
    border-radius:28px 28px 0 0;
    background:linear-gradient(120deg,var(--cream) 0%,var(--sage) 45%,var(--cream) 70%,var(--lilac) 100%);
  }
  .hang-hole{
    position:absolute;left:50%;top:50px;transform:translateX(-50%);
    width:170px;height:40px;border-radius:20px;background:var(--stage);
  }
  .hang-hole::before{
    content:"";position:absolute;left:50%;top:-14px;transform:translateX(-50%);
    width:50px;height:50px;border-radius:50%;background:var(--stage);
  }
  .panel{
    position:absolute;left:0;top:160px;width:100%;height:860px;overflow:hidden;
    background:
      radial-gradient(circle at 85% 20%,var(--sage) 0 18%,transparent 19%),
      radial-gradient(circle at 10% 65%,var(--lilac) 0 14%,transparent 15%),
      radial-gradient(circle at 90% 75%,var(--lilac) 0 16%,transparent 17%),
      radial-gradient(circle at 20% 92%,var(--sage) 0 12%,transparent 13%),
      var(--cream);
    border-top:2px solid var(--cream-deep);
  }
  .photo-window{
    position:absolute;border-radius:70px;
    background:radial-gradient(ellipse at 50% 45%,#3a352c 0 30%,var(--photo) 60%);
    box-shadow:0 0 0 4px #f7f5ec;
  }

  /* back */
  .package--back .photo-window{left:110px;top:70px;width:280px;height:330px}
  .info-label{
    position:absolute;left:85px;top:340px;width:330px;height:350px;
    background:#fafafa;border:3px solid var(--label-edge);border-radius:22px;
  }
  .description{
    position:absolute;left:80px;top:715px;width:340px;
    font-size:15px;line-height:1.45;text-align:center;font-weight:400;
  }
  .cert-row{position:absolute;left:170px;top:815px;display:flex;gap:12px}
  .cert-row span{width:24px;height:24px;border-radius:50%;background:var(--ink)}
  .side-brand{
    position:absolute;right:26px;top:300px;
    writing-mode:vertical-rl;transform:rotate(180deg);
    font-size:30px;font-weight:300;letter-spacing:1px;line-height:1;
  }
  .side-pill{
    position:absolute;right:22px;top:470px;width:38px;height:340px;border-radius:19px;
    background:var(--olive);color:var(--cream);
    writing-mode:vertical-rl;transform:rotate(180deg);
    font-size:13px;display:flex;align-items:center;justify-content:center;gap:14px;
  }
  .side-pill small{color:var(--gold);font-size:10px}

  /* front */
  .tab-model{position:absolute;right:40px;top:108px;font-size:20px}
  .brand-small{position:absolute;left:0;width:100%;top:20px;text-align:center;font-size:20px;font-weight:300}
  .brand-main{position:absolute;left:0;width:100%;top:95px;text-align:center;font-size:56px;font-weight:300;letter-spacing:2px}
  .package--front .photo-window{left:90px;top:210px;width:300px;height:500px}
  .name-band{
    position:absolute;left:0;top:735px;width:390px;height:48px;
    background:var(--olive);border-radius:0 24px 24px 0;
    color:var(--cream);font-size:19px;display:flex;align-items:center;padding-left:70px;
  }
  .front-model{position:absolute;left:70px;top:800px;font-size:18px}
  .accent-arc{position:absolute;width:44px;height:22px;border:6px solid var(--pink);border-top:none;border-radius:0 0 22px 22px}
</style>
</head>
<body>

<section class="package package--back">
  <div class="hang-tab"><div class="hang-hole"></div></div>
  <div class="panel">
    <div class="photo-window" role="img" aria-label="Fotografía de la prenda bodystocking negra de red con liguero"></div>
    <div class="info-label"></div>
    <p class="description">Lorem ipsum dolor sit amet, consectetuer adipiscing elit, sed diam nonummy nibh euismod tincidunt ut laoreet dolore magna aliquam erat volutpat. Ut wisi enim.</p>
    <div class="cert-row" aria-label="Sellos de certificación"><span></span><span></span><span></span><span></span></div>
    <div class="side-brand">Tavrela</div>
    <div class="side-pill">PRODUCT NAME GOES HERE <small>MODELO: 1234</small></div>
  </div>
</section>

<section class="package package--front">
  <div class="hang-tab"><div class="hang-hole"></div><div class="tab-model">MODELO: 1234</div></div>
  <div class="panel">
    <div class="brand-small">Tavrela</div>
    <span class="accent-arc" style="right:40px;top:60px"></span>
    <div class="brand-main">Tavrela</div>
    <div class="photo-window" role="img" aria-label="Fotografía de la modelo usando el bodystocking negro de red"></div>
    <div class="name-band">PRODUCT NAME GOES HERE</div>
    <div class="front-model">MODELO: 1234</div>
  </div>
</section>

</body>
</html>
```